Cloud-based Health 2.0 Web Site

We need the overall look and feel for a new cloud-based Health 2.0 web site where health professionals can manage and interact with their patients/clients.

The plan is to generate a landing page that can grab the attention of health professionals (doctors, nurses, personal trainers, etc...). This page should have an attractive "Sign Up for Free" or similar button/message, as well as a login section for users already registered. We currently have a view on having a number of messages displayed, either as a slider or as separate areas on the page (decision is up for grabs).

Secondly, we need a standard "framework" for all the other pages which will be accessible once the user has authenticated with a clean, airy and spacious feel. This will provide styling for standard elements (input boxes, checkboxes, etc...) as well as a given layout, possibly 3 columns (fixed-fluid-fixed) although we leave this to the designer's choice.

We want to stress the importance of the Cloud, as well as make users feel like "this is the place to be if you're a modern, tech savvy health professional". Also of high importance is to show that this is a secure place, where data is accessible from anywhere yet also highly protected.

This project is going to provide long-term work for the winner and possibly those we consider close runner ups, so if you guys are interested in grabbing our attention so you can become our designer of choice, this is your chance!

Standard pages we are looking to receive after the selection process:

* Landing page
* Health Professional Profile Page (personal details, professional details, photo...)
* Patient list / Patient Management page
* Patient profile (details, health details...)
* Generic "item" management page (item refers to documents, images, contacts, etc...)

The logo for the site/product is also up for grabs, and a bonus payment can be given if you provide one that both matches the style of the site whilst being one that could be reused for mobile app icons, etc...
Updates

The site name is "vitorbis" (all lower-case) for those of you wanting to work on the logo part. As I said before, the logo should contain a component that could be use as the recognisable icon in a mobile phone app. Something that can be easily identified in both the site and the app that connects them together.

vitorbis is made up of two parts (vitor + bis), and you might want to consider differentiating them by the use of colour, fonts or however you think appropriate.

New sample screen-shots of the existing functionality have been uploaded to help you mock up some screens.

PLEASE NOTE: This are to be used for content/widget design only! The layout of how these are represented, e.g. accordion, slider, tree, list... is entirely up to you! Don't guide your layout based on these screen-shots, unless you think they are the way to go, of course. 

We want your creative input, so please innovate! :)

Thanks!

Target Market(s)

Health Professionals

Industry/Entity Type

Health

Requirements
Must have
• * A landing page that grabs the users attention but is "different" from the rest of pages (although within the same design/style parameters)

* A generic page framework for the rest of the pages (style guide)
Nice to have
• A modern and clean logo to go with the site. If the logo is selected, this can result in a bonus payment to be decided.

```html
<!DOCTYPE html>
<html lang="en">
<head>
<meta charset="utf-8">
<title>vitorbis – Professionals</title>
<link rel="stylesheet" href="https://fonts.googleapis.com/css2?family=Arimo:wght@400;700&display=swap">
<style>
:root{
  --blue:#2f6fc4;
  --blue-dark:#1f56a6;
  --blue-light:#4d8ddb;
  --red:#d0121b;
  --red-dark:#a80c13;
  --text:#333;
  --muted:#666;
  --line:#e1e1e1;
  --page:#e4e4e4;
  --panel:#fff;
  --ad:#d6d6d6;
  --footer:#d4d4d4;
}
*{box-sizing:border-box;margin:0;padding:0}
html,body{width:1200px;height:840px;overflow:hidden}
body{position:relative;font-family:"Arimo",Arial,sans-serif;color:var(--text);background:var(--page);font-size:13px}
a{color:inherit;text-decoration:none}

/* header */
.site-header{position:absolute;left:0;top:0;width:1200px;height:100px;background:linear-gradient(#fff,#f3f3f3);border-top:5px solid var(--blue);box-shadow:0 1px 3px rgba(0,0,0,.12)}
.brand{position:absolute;left:120px;top:24px;display:flex;align-items:center;gap:10px}
.brand-mark{width:50px;height:50px;background:var(--blue);border-radius:6px}
.brand-name{font-size:46px;font-weight:400;color:var(--blue);letter-spacing:-1px}
.greeting{position:absolute;left:862px;top:15px;font-size:12px;color:var(--text)}
.logout{position:absolute;left:974px;top:-5px;width:106px;height:38px;background:var(--blue);color:#fff;font-size:14px;display:flex;align-items:center;justify-content:center;gap:8px;border-radius:0 0 3px 3px}
.logout .power{width:18px;height:18px;border-radius:50%;background:var(--red);display:inline-flex;align-items:center;justify-content:center}
.main-nav{position:absolute;top:53px;left:818px;display:flex;gap:32px;font-size:18px;color:#444}
.main-nav a{display:flex;align-items:center;gap:6px}
.chev{width:15px;height:15px;border-radius:50%;background:#555;display:inline-flex;align-items:center;justify-content:center}

/* panels */
.panel{position:absolute;background:var(--panel);border:1px solid #d4d4d4;box-shadow:0 1px 2px rgba(0,0,0,.08)}
.panel-title{height:31px;background:linear-gradient(var(--blue-light),var(--blue));color:#fff;font-weight:700;font-size:14px;line-height:31px;padding-left:14px}
.btn-red{display:inline-block;background:linear-gradient(#e3242c,var(--red));color:#fff;font-size:11px;border-radius:2px;padding:0 9px;line-height:21px}
.btn-blue{display:inline-block;background:linear-gradient(var(--blue-light),var(--blue));color:#fff;font-size:10px;line-height:15px;padding:0 7px;border-radius:2px}
.photo{background:linear-gradient(#d9cfc7,#b59f8c);border:1px solid #ccc}

/* profile */
.profile{left:120px;top:132px;width:182px;height:288px}
.profile .photo{position:absolute;left:14px;top:43px;width:75px;height:77px;background:linear-gradient(#eef1f4,#c9b8a8)}
.login-info{position:absolute;left:98px;top:50px;font-size:12px}
.login-info strong{display:block;color:var(--blue);font-size:14px;margin-bottom:4px}
.login-info .btn-red{margin-top:4px}
.messages{position:absolute;left:0;top:132px;width:100%}
.messages h3{font-size:13px;color:var(--blue);padding:4px 14px;display:flex;gap:7px;align-items:center;border-bottom:1px solid var(--line)}
.messages li{list-style:none;font-size:11px;font-weight:700;padding:7px 14px;border-bottom:1px solid var(--line);display:flex;gap:8px;align-items:center}
.messages li.read{font-weight:400}
.messages .btn-red{margin:10px 14px}

/* social */
.social{left:120px;top:429px;width:182px;height:63px;display:flex;align-items:center;padding-left:12px;gap:10px}
.social-dot{width:28px;height:28px;border-radius:50%;background:#3fa9e0}
.counts{display:flex;flex-direction:column;gap:4px}
.count{display:flex;width:118px;height:24px;border:1px solid #ccc;font-size:12px;align-items:center}
.count b{flex:1;padding-left:8px}
.count span{color:var(--blue);padding-right:8px}

/* nav */
.manage{left:120px;top:502px;width:182px;height:244px}
.side-nav{list-style:none;padding:6px 12px}
.side-nav li{display:flex;align-items:center;gap:14px;height:33px;font-size:16px;color:#555;border-bottom:1px solid var(--line)}
.side-nav li:last-child{border-bottom:0}
.side-nav li.active{color:var(--blue)}
.side-nav svg{width:17px;height:17px;fill:#555}
.side-nav li.active svg{fill:var(--blue)}

/* professionals */
.professionals{left:317px;top:132px;width:564px;height:614px}
.subbar{height:34px;background:linear-gradient(#f4f4f4,#e6e6e6);border-bottom:1px solid #d8d8d8;display:flex;align-items:center;gap:8px;padding-left:14px;font-size:12px;color:#666}
.pro-row{display:flex;height:113px;border-bottom:1px solid var(--line);padding:12px 0 0 14px}
.pro-row:nth-child(odd){background:linear-gradient(#fff,#f6f6f6)}
.pro-card{width:281px;display:flex;gap:10px}
.pro-card .photo{width:77px;height:77px}
.pro-card .photo.alt{background:linear-gradient(#a9b7a0,#b48f78)}
.pro-card .photo.warm{background:linear-gradient(#d7c4a4,#c4a183)}
.pro-info{font-size:11px;color:#555;padding-top:6px;display:flex;flex-direction:column;gap:4px}
.pro-info h4{font-size:12px;color:var(--blue-dark);margin-bottom:2px}
.pro-info p{display:flex;align-items:center;gap:6px}
.pro-info svg{width:11px;height:11px;fill:#777}
.pager{position:absolute;left:14px;top:575px;display:flex;gap:10px;align-items:center;font-size:16px;color:#555}
.pager .arrow{width:22px;height:22px;background:var(--blue);border-radius:2px;display:flex;align-items:center;justify-content:center}
.pager .current{border:1px solid #bbb;padding:0 5px;line-height:20px}
.create-new{position:absolute;left:432px;top:559px;width:117px;height:31px;background:linear-gradient(#e3242c,var(--red-dark));color:#fff;font-size:15px;font-weight:700;display:flex;align-items:center;justify-content:center;border-radius:2px}

/* daily numbers */
.daily{left:897px;top:132px;width:181px;height:219px}
.select{position:absolute;left:14px;top:38px;width:150px;height:26px;border:1px solid #bbb;font-size:11px;color:#888;line-height:24px;padding-left:6px}
.select::after{content:"";position:absolute;right:0;top:0;width:16px;height:24px;background:#222}
.field{position:absolute;left:14px;display:flex;align-items:center;width:160px;font-size:12px}
.field label{width:53px}
.field span{width:96px;height:22px;border:1px solid #bbb;border-radius:3px;color:#aaa;font-size:10px;line-height:20px;padding-left:5px}
.daily .btn-red{position:absolute;left:66px;top:181px;width:76px;text-align:center;font-size:13px;font-weight:700}
.ad{position:absolute;left:897px;width:181px;background:var(--ad);color:#fff;font-size:38px;font-weight:700;line-height:1.1;display:flex;align-items:center;justify-content:center;text-align:center}

/* footer */
.site-footer{position:absolute;left:0;top:780px;width:1200px;height:60px;background:var(--footer)}
.footer-links{position:absolute;left:120px;top:22px;font-size:11px;color:#555;display:flex;gap:9px}
.footer-brand{position:absolute;left:920px;top:12px;display:flex;align-items:center;gap:7px}
.footer-brand i{width:32px;height:32px;background:#fff;border-radius:4px}
.footer-brand span{color:#fff;font-size:30px}
</style>
</head>
<body>
<header class="site-header">
  <div class="brand"><span class="brand-mark"></span><span class="brand-name">vitorbis</span></div>
  <div class="greeting">Hello, Clara Benedetti !</div>
  <a class="logout" href="#">Log Out <span class="power"><svg width="10" height="10" viewBox="0 0 10 10"><path d="M5 1v4M2.5 3A3 3 0 1 0 7.5 3" stroke="#fff" stroke-width="1.4" fill="none"/></svg></span></a>
  <nav class="main-nav">
    <a href="#">Profile <span class="chev"><svg width="8" height="6" viewBox="0 0 8 6"><path d="M1 1l3 3 3-3" stroke="#fff" stroke-width="1.6" fill="none"/></svg></span></a>
    <a href="#">Settings <span class="chev"><svg width="8" height="6" viewBox="0 0 8 6"><path d="M1 1l3 3 3-3" stroke="#fff" stroke-width="1.6" fill="none"/></svg></span></a>
    <a href="#">Options</a>
  </nav>
</header>

<section class="panel profile">
  <div class="panel-title">Dr. Clara Benedetti</div>
  <div class="photo" role="img" aria-label="Portrait photo of the doctor"></div>
  <div class="login-info"><strong>Last Login</strong>20 Jan 2012<br><a class="btn-red" href="#">Edit Profile</a></div>
  <div class="messages">
    <h3><svg width="14" height="10" viewBox="0 0 14 10"><rect width="14" height="10" fill="#2f6fc4"/><path d="M0 0l7 5 7-5" stroke="#fff" fill="none"/></svg>Messages</h3>
    <ul>
      <li><svg width="11" height="8" viewBox="0 0 11 8"><rect width="11" height="8" fill="#333"/></svg>Hello clara benedet...</li>
      <li><svg width="11" height="8" viewBox="0 0 11 8"><rect width="11" height="8" fill="#333"/></svg>Hello clara benedet...</li>
      <li class="read"><svg width="11" height="9" viewBox="0 0 11 9"><path d="M0 4l5.5-4 5.5 4v5H0z" fill="#888"/></svg>Hello clara benedet...</li>
    </ul>
    <a class="btn-red" href="#">Go to inbox</a>
  </div>
</section>

<section class="panel social">
  <span class="social-dot"></span>
  <div class="counts">
    <div class="count"><b>Following</b><span>1,059</span></div>
    <div class="count"><b>Followers</b><span>2,000</span></div>
  </div>
</section>

<section class="panel manage">
  <div class="panel-title">Manage Profile</div>
  <ul class="side-nav">
    <li><svg viewBox="0 0 16 16"><path d="M8 1l7 7h-2v7H10v-5H6v5H3V8H1z"/></svg>Home</li>
    <li><svg viewBox="0 0 16 16"><circle cx="5" cy="5" r="3"/><circle cx="11" cy="6" r="2.5"/><path d="M0 14c0-4 10-4 10 0zM9 13c0-3 7-3 7 0z"/></svg>Patients</li>
    <li class="active"><svg viewBox="0 0 16 16"><path d="M8 0a5 5 0 0 1 5 5c0 4-5 11-5 11S3 9 3 5a5 5 0 0 1 5-5zm0 3a2 2 0 1 0 0 4 2 2 0 0 0 0-4z"/></svg>Professionals</li>
    <li><svg viewBox="0 0 16 16"><path d="M0 2h6c1 0 2 1 2 2 0-1 1-2 2-2h6v11h-6c-1 0-2 1-2 1s-1-1-2-1H0zm2 2v7h5V4zm7 0v7h5V4z"/></svg>Studies</li>
    <li><svg viewBox="0 0 16 16"><path d="M2 0h9l3 3v13H2zm2 5v1h8V5zm0 3v1h8V8zm0 3v1h6v-1z"/></svg>Surveys</li>
    <li><svg viewBox="0 0 16 16"><path d="M11 1l4 4-9 9-5 1 1-5z"/></svg>Designer</li>
  </ul>
</section>

<section class="panel professionals">
  <div class="panel-title">Professionals</div>
  <div class="subbar"><svg width="11" height="13" viewBox="0 0 11 13"><path d="M0 0h8l3 3v10H0z" fill="#777"/></svg>Details</div>
  <div class="pro-list">
    <div class="pro-row">
      <div class="pro-card"><div class="photo" role="img" aria-label="Photo of Marco Reyes"></div><div class="pro-info"><h4>Marco Reyes</h4><p><svg viewBox="0 0 11 11"><rect y="2" width="11" height="7"/></svg>marcoreyes@vitorbis.com</p><p><svg viewBox="0 0 11 11"><circle cx="5.5" cy="3" r="2.5"/><path d="M0 11c0-5 11-5 11 0z"/></svg>03-Nov-1975</p><span><a class="btn-blue" href="#">Full Details</a></span></div></div>
      <div class="pro-card"><div class="photo alt" role="img" aria-label="Photo of Daniel Ortiz"></div><div class="pro-info"><h4>Daniel Ortiz</h4><p><svg viewBox="0 0 11 11"><rect y="2" width="11" height="7"/></svg>danielortiz@vitorbis.com</p><p><svg viewBox="0 0 11 11"><circle cx="5.5" cy="3" r="2.5"/><path d="M0 11c0-5 11-5 11 0z"/></svg>03-Nov-1975</p><span><a class="btn-blue" href="#">Full Details</a></span></div></div>
    </div>
    <div class="pro-row">
      <div class="pro-card"><div class="photo warm" role="img" aria-label="Photo of Lena Hart"></div><div class="pro-info"><h4>Lena Hart</h4><p><svg viewBox="0 0 11 11"><rect y="2" width="11" height="7"/></svg>danielortiz@vitorbis.com</p><p><svg viewBox="0 0 11 11"><circle cx="5.5" cy="3" r="2.5"/><path d="M0 11c0-5 11-5 11 0z"/></svg>03-Nov-1975</p><span><a class="btn-blue" href="#">Full Details</a></span></div></div>
      <div class="pro-card"><div class="photo warm" role="img" aria-label="Photo of Sara Lind"></div><div class="pro-info"><h4>Sara Lind</h4><p><svg viewBox="0 0 11 11"><rect y="2" width="11" height="7"/></svg>danielortiz@vitorbis.com</p><p><svg viewBox="0 0 11 11"><circle cx="5.5" cy="3" r="2.5"/><path d="M0 11c0-5 11-5 11 0z"/></svg>03-Nov-1975</p><span><a class="btn-blue" href="#">Full Details</a></span></div></div>
    </div>
    <div class="pro-row">
      <div class="pro-card"><div class="photo" role="img" aria-label="Photo of Marco Reyes"></div><div class="pro-info"><h4>Marco Reyes</h4><p><svg viewBox="0 0 11 11"><rect y="2" width="11" height="7"/></svg>marcoreyes@vitorbis.com</p><p><svg viewBox="0 0 11 11"><circle cx="5.5" cy="3" r="2.5"/><path d="M0 11c0-5 11-5 11 0z"/></svg>03-Nov-1975</p><span><a class="btn-blue" href="#">Full Details</a></span></div></div>
      <div class="pro-card"><div class="photo alt" role="img" aria-label="Photo of Daniel Ortiz"></div><div class="pro-info"><h4>Daniel Ortiz</h4><p><svg viewBox="0 0 11 11"><rect y="2" width="11" height="7"/></svg>danielortiz@vitorbis.com</p><p><svg viewBox="0 0 11 11"><circle cx="5.5" cy="3" r="2.5"/><path d="M0 11c0-5 11-5 11 0z"/></svg>03-Nov-1975</p><span><a class="btn-blue" href="#">Full Details</a></span></div></div>
    </div>
    <div class="pro-row">
      <div class="pro-card"><div class="photo warm" role="img" aria-label="Photo of Lena Hart"></div><div class="pro-info"><h4>Lena Hart</h4><p><svg viewBox="0 0 11 11"><rect y="2" width="11" height="7"/></svg>danielortiz@vitorbis.com</p><p><svg viewBox="0 0 11 11"><circle cx="5.5" cy="3" r="2.5"/><path d="M0 11c0-5 11-5 11 0z"/></svg>03-Nov-1975</p><span><a class="btn-blue" href="#">Full Details</a></span></div></div>
      <div class="pro-card"><div class="photo warm" role="img" aria-label="Photo of Sara Lind"></div><div class="pro-info"><h4>Sara Lind</h4><p><svg viewBox="0 0 11 11"><rect y="2" width="11" height="7"/></svg>danielortiz@vitorbis.com</p><p><svg viewBox="0 0 11 11"><circle cx="5.5" cy="3" r="2.5"/><path d="M0 11c0-5 11-5 11 0z"/></svg>03-Nov-1975</p><span><a class="btn-blue" href="#">Full Details</a></span></div></div>
    </div>
  </div>
  <nav class="pager">
    <a class="arrow" href="#"><svg width="8" height="10" viewBox="0 0 8 10"><path d="M6 1L2 5l4 4" stroke="#fff" stroke-width="2" fill="none"/></svg></a>
    <span class="current">1</span><a href="#">2</a><a href="#">3</a><a href="#">4</a><a href="#">5</a>
    <a class="arrow" href="#"><svg width="8" height="10" viewBox="0 0 8 10"><path d="M2 1l4 4-4 4" stroke="#fff" stroke-width="2" fill="none"/></svg></a>
  </nav>
  <a class="create-new" href="#">Create New</a>
</section>

<section class="panel daily">
  <div class="panel-title">My Daily Numbers</div>
  <div class="select">Blood Pressure</div>
  <div class="field" style="top:85px"><label>Diastolic</label><span>mmHg</span></div>
  <div class="field" style="top:117px"><label>Systolic</label><span>mmHg</span></div>
  <div class="field" style="top:149px"><label>Date</label><span>DD/MM/YYYY</span></div>
  <a class="btn-red" href="#">Submit</a>
</section>

<aside class="ad" style="top:362px;height:218px">Add<br>Space</aside>
<aside class="ad" style="top:591px;height:155px">Add<br>Space</aside>

<footer class="site-footer">
  <nav class="footer-links"><a href="#">About Us</a>|<a href="#">Pricing</a>|<a href="#">FAQ</a>|<a href="#">Contact Us</a></nav>
  <div class="footer-brand"><i></i><span>vitorbis</span></div>
</footer>
</body>
</html>
```